Business Card Design Project

We need business cards for our new business, Vantrel Optics. We specialize in aerial videography and photography via drone. Currently we are mainly focusing on real estate videography but will branch into other markets and may even host training classes for flying drones.
Updates
Cards should include:
Name
Phone Number
Email Address
Web address
We will need to customize for more than one person and would like those fields to be editable
eps file logos are uploaded now, thanks!
Target Market(s)
Real Estate Agents, hotels, rental agencies and people who have recently purchase drones
Industry/Entity Type
Videography
Font styles to use
Look and feel
Each slider illustrates characteristics of the customer's brand and the style your logo design should communicate.

```html
<!DOCTYPE html>
<html lang="en">
<head>
<meta charset="utf-8">
<title>Vantrel Optics – Business Card</title>
<link rel="stylesheet" href="https://fonts.googleapis.com/css2?family=Arimo:wght@400&display=swap">
<style>
  :root {
    --backdrop: #e9e6e1;
    --card-dark: #0b0b0c;
    --card-glow: #4a4a4c;
    --card-orange: #efa00e;
    --ink-light: #ffffff;
    --ink-dark: #2a2217;
    --card-shadow: rgba(0, 0, 0, 0.28);
  }
  * { box-sizing: border-box; margin: 0; padding: 0; }
  html, body {
    width: 1200px;
    height: 533px;
    overflow: hidden;
    background: var(--backdrop);
    font-family: "Arimo", Arial, sans-serif;
  }
  .card-spread {
    position: absolute;
    left: 120px;
    top: 127px;
    width: 960px;
    height: 279px;
    display: flex;
    box-shadow: 0 4px 12px var(--card-shadow);
  }
  .card-front {
    position: relative;
    width: 480px;
    height: 100%;
    background:
      radial-gradient(ellipse 190px 150px at 50% 100%, var(--card-glow) 0%, rgba(74,74,76,0) 100%),
      var(--card-dark);
  }
  .brand {
    position: absolute;
    left: 96px;
    top: 113px;
    display: flex;
    align-items: center;
    gap: 12px;
  }
  .brand-square {
    width: 30px;
    height: 30px;
    background: var(--card-orange);
  }
  .brand-name {
    color: var(--ink-light);
    font-size: 29px;
    font-weight: 400;
    letter-spacing: 1px;
    text-transform: uppercase;
  }
  .card-back {
    position: relative;
    width: 480px;
    height: 100%;
    background: var(--card-orange);
    color: var(--ink-dark);
  }
  .holder-name {
    position: absolute;
    left: 248px;
    top: 131px;
    font-size: 16px;
    letter-spacing: 0.4px;
    text-transform: uppercase;
  }
  .address {
    position: absolute;
    left: 249px;
    top: 166px;
    font-size: 11px;
    line-height: 13.5px;
    font-style: normal;
  }
  .contact-list {
    position: absolute;
    left: 249px;
    top: 226px;
    list-style: none;
    font-size: 11px;
    line-height: 13px;
  }
  .contact-list li {
    display: flex;
    align-items: center;
    gap: 3px;
  }
  .contact-icon {
    width: 8px;
    height: 8px;
    flex: none;
  }
</style>
</head>
<body>
  <main class="card-spread">
    <section class="card-front">
      <div class="brand">
        <span class="brand-square"></span>
        <span class="brand-name">Vantrel Optics</span>
      </div>
    </section>
    <section class="card-back">
      <h1 class="holder-name">Rohan Vesh</h1>
      <address class="address">
        214, Cedar Park Homes,<br>
        2nd Cross, 6th main,<br>
        KL Colony, East Layout,<br>
        Harwick Nagar, Northvale-560 042
      </address>
      <ul class="contact-list">
        <li>
          <svg class="contact-icon" viewBox="0 0 8 8" aria-hidden="true"><rect x="1.5" y="0.5" width="5" height="7" rx="0.8" fill="#2a2217"/><rect x="2.5" y="1.5" width="3" height="4" fill="#efa00e"/></svg>
          90412 577 18
        </li>
        <li>
          <svg class="contact-icon" viewBox="0 0 8 8" aria-hidden="true"><rect x="0.5" y="1.5" width="7" height="5" fill="none" stroke="#2a2217"/><path d="M0.5 1.5 L4 4.5 L7.5 1.5" fill="none" stroke="#2a2217" stroke-width="0.8"/></svg>
          info@vantrel.com
        </li>
        <li>
          <svg class="contact-icon" viewBox="0 0 8 8" aria-hidden="true"><rect x="0.5" y="0.5" width="7" height="7" fill="none" stroke="#2a2217"/><rect x="2.5" y="2.5" width="3" height="3" fill="#2a2217"/></svg>
          vantrel.com
        </li>
      </ul>
    </section>
  </main>
</body>
</html>
```